Unique vibrant packaging design for Lime coloured Cosmetic sponge launching in retail stores.

We are an Irish based company specialising in Cosmetic tools and accesories. We would like a packaging design for our costmetic sponge which is an innovative design which we feel deserves a unique pakaging design also. Our target market is young,creative people and our brand is all about colour and vibrancy. We look forward to the design process and hope to work with creative designers.

The box packaging will be PET Plastic in the shape shown in the images attached to the draft. the size is -
Height- 7cm
Width- 5cm
Depth- 5cm.

Description of product to be displayed on packaging:

Achieve Flawless skin with Dew Petal Pad. Blend Liquids and cream products effortlessly for a seamless and flawless finish. Latex Free.

www.quillandtarn.com

Target Market(s)

Beauty products enthusiasts

Industry/Entity Type

Hair And Beauty

Colors
f9d9e8
e4daeb
d3a5cc
fefdfe

Requirements
Must have
• Eye Catching,simple concept. A light shade of pink.
Nice to have
• Bokeh effect,faded colour,simple geometric design.
Should not have
• Any colour other than Pink,light purples.

```html
<!DOCTYPE html>
<html lang="en">
<head>
<meta charset="utf-8">
<title>Dew Petal Pad – Packaging Front</title>
<link rel="stylesheet" href="https://fonts.googleapis.com/css2?family=Bebas+Neue&display=swap">
<style>
  :root {
    --paper: #ffffff;
    --magenta: #e6007e;
    --magenta-soft: rgba(230, 0, 126, 0.55);
    --ink: #000000;
    --logo-text: #ffffff;
  }
  html, body {
    margin: 0;
    padding: 0;
    overflow: hidden;
    background: var(--paper);
  }
  .pack-front {
    position: relative;
    width: 857px;
    height: 1200px;
    overflow: hidden;
    background: var(--paper);
    font-family: "Bebas Neue", "Arial Narrow", sans-serif;
  }
  .product-title {
    position: absolute;
    left: 80px;
    top: 48px;
    margin: 0;
    font-weight: 400;
    font-size: 138px;
    line-height: 123px;
    letter-spacing: 1px;
    color: var(--magenta);
    text-transform: uppercase;
  }
  .product-title span { display: block; }
  .dot-field {
    position: absolute;
    inset: 0;
    width: 857px;
    height: 1200px;
  }
  .brand-badge {
    position: absolute;
    left: 492px;
    top: 860px;
    width: 292px;
    height: 292px;
    border-radius: 50%;
    background: var(--ink);
    display: flex;
    align-items: center;
    justify-content: center;
  }
  .brand-name {
    color: var(--logo-text);
    font-size: 58px;
    line-height: 1;
    letter-spacing: 2px;
    text-align: center;
  }
</style>
</head>
<body>
  <main class="pack-front">
    <svg class="dot-field" viewBox="0 0 857 1200" role="img" aria-label="Magenta halftone dot pattern sweeping up from the lower left to the upper right corner">
      <defs>
        <radialGradient id="dotFade" cx="857" cy="1200" r="1250" gradientUnits="userSpaceOnUse">
          <stop offset="0" stop-color="#e6007e" stop-opacity="0.6"/>
          <stop offset="0.45" stop-color="#e6007e" stop-opacity="0.28"/>
          <stop offset="0.8" stop-color="#e6007e" stop-opacity="0.05"/>
          <stop offset="1" stop-color="#e6007e" stop-opacity="0"/>
        </radialGradient>
      </defs>
      <path d="M857 0 C 700 300, 420 620, 0 760 L 0 1200 L 857 1200 Z" fill="url(#dotFade)"/>
    </svg>

    <h1 class="product-title">
      <span>Dew</span>
      <span>Petal</span>
      <span>Pad</span>
    </h1>

    <div class="brand-badge">
      <div class="brand-name">Quill<br>&amp; Tarn</div>
    </div>
  </main>
</body>
</html>
```